Website for Company that serves and supports Investment Banks

We are seeking to have a six page website that provides a basic description of our company's services. Our company provides Financial Models and Investment Memos on an outsourced basis to Small Investment Banks and Investment firms. We do not require a shopping cart. We already have a logo attached.

Target Market(s)

Small, regional investment banks. Small private equity firms.

Industry/Entity Type

Finance And Accounting

Coding

Coded - Design and coding required

Number of Pages Required

5+ page

Requirements
Nice to have
• Please use the logo design to drive how you design the layout for the website

```html
<!DOCTYPE html>
<html lang="en">
<head>
<meta charset="utf-8">
<title>NorthgateAnalyst.com</title>
<link href="https://fonts.googleapis.com/css2?family=Open+Sans:wght@400;600;700&family=Oswald:wght@400;500&family=Roboto:wght@400;500&display=swap" rel="stylesheet">
<style>
:root{
  --blue:#1b78c2;
  --blue-dark:#0e5a9e;
  --blue-deep:#0a3f86;
  --nav-top:#2a8fd6;
  --nav-bottom:#1466ad;
  --ink:#222;
  --text:#3a3a3a;
  --muted:#666;
  --light:#f2f2f2;
  --footer:#2b2b2b;
  --footer-text:#d8d8d8;
  --white:#fff;
}
*{box-sizing:border-box;margin:0;padding:0}
html,body{width:1200px;height:3371px;overflow:hidden}
body{position:relative;background:var(--white);font-family:"Open Sans",Arial,sans-serif;color:var(--text)}
.abs{position:absolute}

/* header */
.site-header{left:0;top:0;width:1200px;height:124px;background:var(--white)}
.brand{left:0;width:1200px;top:24px;text-align:center}
.brand-mark{display:inline-block;width:46px;height:46px;border-radius:50%;background:var(--blue-dark);vertical-align:middle;margin-right:12px}
.brand-name{display:inline-block;vertical-align:middle;font-family:"Roboto",sans-serif;font-weight:500;font-size:26px;color:var(--blue-deep)}
.brand-tag{left:0;width:1200px;top:86px;text-align:center;font-size:12px;letter-spacing:2px;color:var(--blue-deep)}

.main-nav{left:0;top:124px;width:1200px;height:63px;background:linear-gradient(var(--nav-top),var(--nav-bottom))}
.main-nav ul{list-style:none;display:flex;position:absolute;left:90px;top:0;height:63px}
.main-nav li{height:63px;line-height:63px;color:var(--white);font-size:17px;padding:0 36px}
.main-nav li.active{background:var(--blue-dark);padding:0 40px}
.main-nav li:nth-child(2){margin-left:4px}
.main-nav li:nth-child(3){margin-left:20px}
.main-nav li:nth-child(4){margin-left:18px}
.main-nav li:nth-child(5){margin-left:18px}
.main-nav li:nth-child(6){margin-left:22px}

/* hero */
.hero{left:0;top:187px;width:1200px;height:483px;background:linear-gradient(115deg,#7b8896 0%,#b8c2cc 35%,#e6e9ec 55%,#9aa3ac 80%,#5f6770 100%)}
.hero-title-box{left:90px;top:240px;width:495px;height:124px;background:rgba(60,60,60,.55);padding:18px 22px}
.hero-title{font-family:"Oswald",sans-serif;font-size:44px;line-height:50px;color:var(--white);font-weight:500}
.hero-sub{font-family:"Oswald",sans-serif;font-size:22px;color:var(--white);margin-top:4px}
.hero-arrows{right:82px;top:432px;display:flex;gap:2px}
.hero-arrows span{width:16px;height:20px;background:#555;display:block}

/* about */
.about-block{left:83px;top:775px;width:317px;height:330px;background:var(--blue)}
.about-photo{left:108px;top:804px;width:314px;height:328px;background:linear-gradient(160deg,#f6f4ef 0%,#d9cfc0 40%,#7b8ea6 75%,#3b4f6b 100%);box-shadow:0 4px 14px rgba(0,0,0,.25)}
.about-title{left:460px;top:778px;font-family:"Roboto",sans-serif;font-size:32px;color:var(--ink)}
.about-text{left:460px;top:832px;width:670px;font-size:14.5px;line-height:22px;color:var(--text)}
.about-text p{margin-bottom:22px}
.btn-pill{display:inline-block;border-radius:18px;font-size:12px;text-transform:uppercase}
.about-btn{left:454px;top:1096px;width:112px;height:32px;line-height:32px;text-align:center;background:#4aa7e3;color:var(--white)}

/* why hire */
.why{left:0;top:1220px;width:1200px;height:470px;background:linear-gradient(90deg,var(--blue-deep),var(--blue) 60%)}
.why-photo{left:675px;top:1220px;width:525px;height:470px}
.why-title{left:78px;top:1290px;font-family:"Roboto",sans-serif;font-size:31px;color:var(--white)}
.why-list{left:78px;top:1352px;width:565px;list-style:none;color:var(--white);font-size:14.5px;line-height:21px}
.why-list li{position:relative;padding-left:32px;margin-bottom:13px}
.bullet{position:absolute;left:0;top:3px;width:16px;height:16px}
.why-btn{left:80px;top:1598px;width:116px;height:38px;line-height:36px;text-align:center;border:1.5px solid var(--white);color:var(--white);font-size:14px;text-transform:none;border-radius:19px}

/* products */
.products-title{left:0;width:1200px;top:1795px;text-align:center;font-family:"Roboto",sans-serif;font-size:33px;color:var(--ink)}
.product-card{top:1878px;height:392px;background:var(--white);border:2px solid #cfcfcf;box-shadow:0 3px 10px rgba(0,0,0,.35);padding:36px 0 0 52px}
.card-left{left:85px;width:488px}
.card-right{left:604px;width:510px;padding-left:34px}
.card-title{font-family:"Open Sans",sans-serif;font-size:23px;color:var(--blue-dark);text-transform:uppercase;margin-bottom:22px}
.group-title{font-size:21px;color:var(--ink);position:relative;padding-left:30px;margin-top:8px}
.group-title::before{content:"\00bb";position:absolute;left:0;top:-2px;font-size:24px}
.price-row{display:flex;font-size:16px;line-height:28px;color:var(--text);padding-left:22px}
.price-row .item{width:290px}
.card-right .price-row .item{width:342px}
.gap{height:30px}
.card-right .group-title{margin-top:2px}

/* intake */
.intake{left:0;top:2375px;width:1200px;height:697px;background:linear-gradient(180deg,#eaeaea,#f7f7f7 30%,#ececec)}
.intake-title{left:0;width:1200px;top:2468px;text-align:center;font-family:"Roboto",sans-serif;font-size:33px;color:var(--ink)}
.intake-list{left:155px;top:2552px;width:920px;list-style:none;font-size:15px;line-height:25px;color:var(--text)}
.intake-list li{position:relative;padding-left:38px;margin-bottom:17px}
.intake-list .bullet{top:4px;width:17px;height:17px}

/* footer */
.site-footer{left:0;top:3072px;width:1200px;height:299px;background:var(--footer);color:var(--footer-text)}
.foot-h{top:3124px;font-size:15px;color:var(--white);text-transform:uppercase}
.foot-links{left:97px;top:3156px;list-style:none;font-size:11.5px;line-height:24px}
.foot-contact{left:344px;top:3156px;font-size:11.5px;line-height:24px}
.foot-contact div{position:relative;padding-left:24px}
.foot-contact svg{position:absolute;left:0;top:6px}
.foot-mail-text{left:645px;top:3154px;width:210px;font-size:11.5px;line-height:18px}
.mail-field{left:645px;top:3200px;width:145px;height:30px;background:var(--white);color:#888;font-size:11px;line-height:30px;padding-left:10px}
.mail-btn{left:790px;top:3200px;width:63px;height:30px;background:var(--blue);color:var(--white);font-size:11.5px;line-height:30px;text-align:center}
.social{left:937px;top:3166px;display:flex;gap:14px}
.social span{width:25px;height:25px;background:#e4e4e4;border-radius:4px;display:block}
.foot-rule{left:97px;top:3296px;width:1013px;height:1px;background:#444}
.copyright{left:0;width:1200px;top:3322px;text-align:center;font-size:12.5px;color:var(--white)}
</style>
</head>
<body>

<header class="site-header abs">
  <div class="brand abs"><span class="brand-mark"></span><span class="brand-name">NorthgateAnalyst.com</span></div>
  <div class="brand-tag abs">Outsourced Financial Analyst Partners</div>
</header>

<nav class="main-nav abs">
  <ul>
    <li class="active">Home</li>
    <li>About us</li>
    <li>Leadership</li>
    <li>Product Offering</li>
    <li>Process Works</li>
    <li>Contact Us</li>
  </ul>
</nav>

<section class="hero abs" role="img" aria-label="Businessman working with a calculator and laptop at a desk, overlaid with a world network map"></section>
<div class="hero-title-box abs">
  <h1 class="hero-title">NORTHGATE ANALYST</h1>
  <div class="hero-sub">Small Investment Banks and Investment firms</div>
</div>
<div class="hero-arrows abs"><span></span><span></span></div>

<div class="about-block abs"></div>
<div class="about-photo abs" role="img" aria-label="Businessman holding a tablet blended with a city skyline at sunrise"></div>
<h2 class="about-title abs">About us</h2>
<div class="about-text abs">
  <p>NorthgateAnalyst.com functions as an outsourced Financial Analyst partner for smaller, regional investment banks, private equity firms, business brokers, and mezzanine loan funds.</p>
  <p>We focus exclusively on lower middle-market clients.</p>
  <p>We believe Financial Models and Investment Memos are two of the most important deal support tools for executing private equity and investment banking transactions.</p>
  <p>NorthgateAnalyst.com specializes in delivering robust LBO, Growth Equity, Recap and Merger</p>
  <p>NorthgateAnalyst.com specializes in delivering high quality Investment Memos and Investor</p>
</div>
<div class="about-btn btn-pill abs">Read more &raquo;</div>

<section class="why abs"></section>
<svg class="why-photo abs" viewBox="0 0 525 470" role="img" aria-label="Businessman watering a plant shaped like a rising growth chart in front of a city skyline">
  <defs><linearGradient id="whyFill" x1="0" y1="0" x2="0" y2="1"><stop offset="0" stop-color="#c9cdd1"/><stop offset=".6" stop-color="#e4e6e8"/><stop offset="1" stop-color="#9ea4a9"/></linearGradient></defs>
  <polygon points="95,0 525,0 525,470 0,470" fill="url(#whyFill)"/>
</svg>
<h2 class="why-title abs">Why Hire NorthgateAnalyst.com?</h2>
<ul class="why-list abs">
  <li><svg class="bullet" viewBox="0 0 16 16"><circle cx="8" cy="8" r="8" fill="#fff"/><path d="M6.5 4.5 10 8l-3.5 3.5" stroke="#0e5a9e" stroke-width="2" fill="none"/></svg>We are much more cost-effective than hiring full-time Analyst pool</li>
  <li><svg class="bullet" viewBox="0 0 16 16"><circle cx="8" cy="8" r="8" fill="#fff"/><path d="M6.5 4.5 10 8l-3.5 3.5" stroke="#0e5a9e" stroke-width="2" fill="none"/></svg>We give You the ability to purchase Financial Models and Investment Memos on a “product-by-product” on demand basis with standardized prices</li>
  <li><svg class="bullet" viewBox="0 0 16 16"><circle cx="8" cy="8" r="8" fill="#fff"/><path d="M6.5 4.5 10 8l-3.5 3.5" stroke="#0e5a9e" stroke-width="2" fill="none"/></svg>Cost of our Financial Models and Investment Memos is less expensive than other outsourced dealproviders including investment bankers, attorneys, accountants and industry consultants.</li>
  <li><svg class="bullet" viewBox="0 0 16 16"><circle cx="8" cy="8" r="8" fill="#fff"/><path d="M6.5 4.5 10 8l-3.5 3.5" stroke="#0e5a9e" stroke-width="2" fill="none"/></svg>Cost of our Financial Models and Investment Memos is less expensive than Quality of Earnings Analysis reports provided by accounting firms</li>
</ul>
<div class="why-btn btn-pill abs">Read More</div>

<h2 class="products-title abs">PRODUCT OFFERING</h2>
<div class="product-card card-left abs">
  <h3 class="card-title">Financial Models:</h3>
  <div class="group-title">Deal Transaction Models:</div>
  <div class="price-row"><span class="item">LBO, Growth Equity, Recap</span><span>$3,500</span></div>
  <div class="gap"></div>
  <div class="group-title">Valuation Models:</div>
  <div class="price-row"><span class="item">Discounted Cashflow</span><span>$2,500</span></div>
  <div class="price-row"><span class="item">Comparable Company Analysis</span><span>$1,000</span></div>
  <div class="price-row"><span class="item">Private Multiple Analysis</span><span>$1,000</span></div>
</div>
<div class="product-card card-right abs">
  <h3 class="card-title">Investment Documents:</h3>
  <div class="group-title">Investment Memos:</div>
  <div class="price-row"><span class="item">15-20 page Investment Memo</span><span>$3,500</span></div>
  <div class="price-row"><span class="item">15-20 page Investor Powerpoint</span><span>$3,500</span></div>
  <div class="price-row"><span class="item">40-50 page CIM</span><span>$6,500</span></div>
  <div class="group-title">Deal Support Memos:</div>
  <div class="price-row"><span class="item">2 Executive Summary Teaser Document</span><span>$500</span></div>
  <div class="price-row"><span class="item">2 Page Investment Screening Memo</span><span>$500</span></div>
  <div class="price-row"><span class="item">Customized Industry Research</span><span>$500</span></div>
  <div class="price-row"><span class="item">Customized Company Research</span><span>$500</span></div>
</div>

<section class="intake abs"></section>
<h2 class="intake-title abs">How Our Client Intake Process Works?</h2>
<ul class="intake-list abs">
  <li><svg class="bullet" viewBox="0 0 16 16"><circle cx="8" cy="8" r="8" fill="#0e4f8f"/><path d="M6.5 4.5 10 8l-3.5 3.5" stroke="#fff" stroke-width="2" fill="none"/></svg>Call or email us a brief two sentence description of your deal project and indicate whether you are interested in our Financial Model or Investment Memo products.</li>
  <li><svg class="bullet" viewBox="0 0 16 16"><circle cx="8" cy="8" r="8" fill="#0e4f8f"/><path d="M6.5 4.5 10 8l-3.5 3.5" stroke="#fff" stroke-width="2" fill="none"/></svg>A NorthgateAnalyst client service rep will contact you within 24 hours.</li>
  <li><svg class="bullet" viewBox="0 0 16 16"><circle cx="8" cy="8" r="8" fill="#0e4f8f"/><path d="M6.5 4.5 10 8l-3.5 3.5" stroke="#fff" stroke-width="2" fill="none"/></svg>To ensure confidentiality, we will request that you forward a copy of your Non-Disclosure Agreement for our execution.</li>
  <li><svg class="bullet" viewBox="0 0 16 16"><circle cx="8" cy="8" r="8" fill="#0e4f8f"/><path d="M6.5 4.5 10 8l-3.5 3.5" stroke="#fff" stroke-width="2" fill="none"/></svg>In order for us to get our arms around the transaction we will email you a blank Sources &amp; Uses of Funds template. We will request that you populate this template with all necessary “Flow-of- Funds” information for your transaction.</li>
  <li><svg class="bullet" viewBox="0 0 16 16"><circle cx="8" cy="8" r="8" fill="#0e4f8f"/><path d="M6.5 4.5 10 8l-3.5 3.5" stroke="#fff" stroke-width="2" fill="none"/></svg>You email us all of the basic information we would need to create your Financial Model including historical financials, internal management projections, any relevant depreciation, amortization or debt paydown schedules as well as information about the terms of each tranche of debt.</li>
  <li><svg class="bullet" viewBox="0 0 16 16"><circle cx="8" cy="8" r="8" fill="#0e4f8f"/><path d="M6.5 4.5 10 8l-3.5 3.5" stroke="#fff" stroke-width="2" fill="none"/></svg>You email us to us all of the basic information we would need to create your Investment Memo including internal Company Overview documents, internal industry information, management team bios, relevant website content, and any relevant strategic planning documents.</li>
  <li><svg class="bullet" viewBox="0 0 16 16"><circle cx="8" cy="8" r="8" fill="#0e4f8f"/><path d="M6.5 4.5 10 8l-3.5 3.5" stroke="#fff" stroke-width="2" fill="none"/></svg>We email You a completed Financial Model or Investment Memo within 72 hours.</li>
</ul>

<footer class="site-footer abs"></footer>
<div class="foot-h abs" style="left:97px">Information</div>
<ul class="foot-links abs">
  <li>&raquo; Privacy Policy</li>
  <li>&raquo; Login</li>
  <li>&raquo; Advanced Search</li>
  <li>&raquo; Contact Us</li>
</ul>
<div class="foot-h abs" style="left:344px">Contact Us</div>
<div class="foot-contact abs">
  <div><svg width="10" height="13" viewBox="0 0 10 13"><path d="M5 0a5 5 0 0 1 5 5c0 3.5-5 8-5 8S0 8.5 0 5a5 5 0 0 1 5-5z" fill="#ddd"/><circle cx="5" cy="5" r="2" fill="#2b2b2b"/></svg>410 Harbor Street<br>Suite 7-220 Easton, MA 02300</div>
  <div><svg width="11" height="11" viewBox="0 0 11 11"><path d="M2 0l2 2.5-1 1.5a6 6 0 0 0 3.5 3.5l1.5-1L11 9l-1.5 2C5 11 0 6 0 1.5z" fill="#ddd"/></svg>555-014-2290</div>
  <div><svg width="12" height="9" viewBox="0 0 12 9"><rect width="12" height="9" fill="#ddd"/><path d="M0 0l6 5 6-5" stroke="#2b2b2b" fill="none"/></svg>info@northgateanalyst.com</div>
</div>
<div class="foot-h abs" style="left:645px">Join Our Mailing List</div>
<div class="foot-mail-text abs">Your about us information would fit here nicely.</div>
<div class="mail-field abs">Email address</div>
<div class="mail-btn abs">Submit</div>
<div class="foot-h abs" style="left:937px">Follow Us Out There</div>
<div class="social abs"><span></span><span></span><span></span><span></span></div>
<div class="foot-rule abs"></div>
<div class="copyright abs">Copyright © 2017 All Rights Reserved</div>

</body>
</html>
```